Independent manufacturing consultant needs a professional Logo & biz card Update

I want a new logo using the existing one as inspiration. The company legal name is Brindlecourt Process Advisory & Engineering Group, Inc. Often the name is shortened to Brindlecourt PAE and that matches with web address of www.brindlecourt-pae.example. #1 create a new logo and #2 update biz card. I will need vector file to get cards printed (bilingual English & Japanese). The reverse side will be an exact copy of the original design but in Japanese. I have another resource for the translation so that is not in this scope.
Next month, a follow-up project will be to update the website using new logo and get a professional, cohesive look to all the pages.
Check out web site to get an idea of what we do. The desire is to project professional, articulate, clean, dependable, detailed oriented team of experts.

Target Market(s)

Food and Beverage manufactures. Major players, regiona, and start ups.

Industry/Entity Type

It Company

Contact Information for Business Card

exisiting card and logo provided as foundation but ready to improve upon both!

Logo Text

Brindlecourt PAE or other....

Font styles to use
Sans Serif

Colors
9bcb3c
0356a4

Requirements
Must have
• Logo and biz card.
• Logo will be used for other materials and website.
Nice to have
• open to suggestions.
• Like the Green & Blue colors but also dig grey scale as the website incorporates.
• Open to suggestions.
Should not have
• not to animated. I work with more conservative clients.

```html
<!DOCTYPE html>
<html lang="en">
<head>
<meta charset="utf-8">
<title>Brindlecourt PAE – Business Card</title>
<link rel="stylesheet" href="https://fonts.googleapis.com/css2?family=Roboto:wght@300;400;700;900&display=swap">
<style>
  :root {
    --brand-blue: #0356a4;
    --sky-blue: #2a97d4;
    --brand-green: #9bcb3c;
    --ink: #1e1e1e;
    --paper: #ffffff;
    --stage: #e9e9ea;
    --card-shadow: rgba(0, 0, 0, 0.18);
  }
  * { box-sizing: border-box; margin: 0; padding: 0; }
  html, body {
    width: 1200px; height: 858px; overflow: hidden;
    background: var(--stage);
    font-family: "Roboto", Arial, sans-serif;
  }
  .stage {
    width: 1200px; height: 858px;
    display: flex; flex-direction: column;
    align-items: center; justify-content: center; gap: 44px;
  }
  .card {
    position: relative;
    width: 600px; height: 343px;
    background: var(--paper);
    box-shadow: 0 6px 20px var(--card-shadow);
    overflow: hidden;
  }
  .card__wave { position: absolute; inset: 0; width: 100%; height: 100%; }

  .wordmark {
    font-weight: 900; color: var(--brand-blue);
    letter-spacing: -0.5px; line-height: 1; white-space: nowrap;
  }
  .tagline {
    font-weight: 700; color: var(--ink); text-transform: uppercase;
    letter-spacing: 0.2px; white-space: nowrap;
  }

  /* front */
  .front .brand { position: absolute; left: 34px; top: 42px; }
  .front .wordmark { font-size: 34px; }
  .front .tagline { font-size: 10.5px; margin-top: 8px; }

  .contacts { position: absolute; left: 34px; top: 150px; list-style: none; }
  .contacts li {
    display: flex; align-items: center; gap: 12px;
    font-size: 15px; font-weight: 400; color: var(--ink);
    margin-bottom: 12px;
  }
  .contacts .icon {
    width: 20px; height: 20px; background: var(--brand-blue);
    display: flex; align-items: center; justify-content: center; flex: none;
  }

  .person { position: absolute; right: 52px; top: 40px; text-align: left; }
  .person__name { font-size: 17px; font-weight: 400; color: var(--ink); letter-spacing: 0.3px; }
  .person__role { font-size: 14px; font-weight: 400; color: var(--sky-blue); margin-top: 2px; }

  /* back */
  .back { display: flex; align-items: center; justify-content: center; }
  .back .brand { text-align: center; }
  .back .wordmark { font-size: 46px; }
  .back .tagline { font-size: 13px; margin-top: 12px; letter-spacing: 1px; }
</style>
</head>
<body>
<main class="stage">

  <section class="card front" aria-label="Business card front">
    <svg class="card__wave" viewBox="0 0 600 343" preserveAspectRatio="none" aria-hidden="true">
      <defs>
        <linearGradient id="waveBlue" x1="0" y1="1" x2="1" y2="0">
          <stop offset="0" stop-color="#2a97d4"/>
          <stop offset="0.6" stop-color="#1f78c2"/>
          <stop offset="1" stop-color="#0356a4"/>
        </linearGradient>
      </defs>
      <path d="M250 343 C330 330 370 250 430 180 C480 120 530 70 600 56 L600 343 Z" fill="url(#waveBlue)"/>
      <path d="M232 343 C320 325 360 235 420 160 C470 95 520 40 600 22 L600 44 C530 58 485 110 440 165 C380 240 335 325 255 343 Z" fill="#9bcb3c"/>
      <path d="M228 343 C318 322 355 232 416 156 C466 92 518 36 600 16" fill="none" stroke="#9bcb3c" stroke-width="1.5"/>
    </svg>

    <div class="brand">
      <div class="wordmark">BRINDLECOURT PAE</div>
      <div class="tagline">Process Advisory &amp; Engineering Group</div>
    </div>

    <ul class="contacts">
      <li>
        <span class="icon"><svg width="12" height="12" viewBox="0 0 24 24"><path fill="#fff" d="M6.6 10.8a15.1 15.1 0 0 0 6.6 6.6l2.2-2.2a1 1 0 0 1 1-.25 11.4 11.4 0 0 0 3.6.57 1 1 0 0 1 1 1V20a1 1 0 0 1-1 1A17 17 0 0 1 3 4a1 1 0 0 1 1-1h3.5a1 1 0 0 1 1 1c0 1.25.2 2.45.57 3.57a1 1 0 0 1-.25 1z"/></svg></span>
        555.014 2876
      </li>
      <li>
        <span class="icon"><svg width="12" height="12" viewBox="0 0 24 24"><circle cx="12" cy="12" r="9" fill="none" stroke="#fff" stroke-width="2"/><path d="M3 12h18M12 3c3 3 3 15 0 18M12 3c-3 3-3 15 0 18" fill="none" stroke="#fff" stroke-width="1.6"/></svg></span>
        www.brindlecourt-pae.example
      </li>
      <li>
        <span class="icon"><svg width="12" height="12" viewBox="0 0 24 24"><rect x="3" y="6" width="18" height="12" fill="none" stroke="#fff" stroke-width="2"/><path d="M3 6l9 7 9-7" fill="none" stroke="#fff" stroke-width="2"/></svg></span>
        dana@brindlecourt-pae.example
      </li>
    </ul>

    <div class="person">
      <div class="person__name">DANA WHITCOMBE</div>
      <div class="person__role">Principal</div>
    </div>
  </section>

  <section class="card back" aria-label="Business card back">
    <div class="brand">
      <div class="wordmark">BRINDLECOURT PAE</div>
      <div class="tagline">Process Advisory &amp; Engineering Group</div>
    </div>
  </section>

</main>
</body>
</html>
```